Flyer Design for an electrical company

Hi i need a flyer designed for an electrical contracting company.
Company is based in Sydney, Australia.
We service the domestic market

This flyer will have general information about our services, our guarantees which are the important bit and a couple of offer boxes
E.g. save $97 complimentary electrical safety inspection, save $50 off your job, free power point replacement

Flyer to be two sided

size of flyer is DL, (210mm x 99mm)

Target Market(s)

Home owners

Industry/Entity Type

Electrical

Requirements
Must have
• Offer boxes save $97 complimentry electrical safety inspection,Save $50 off your job,free power point replacment, Save $150 OFF switchboard upgrades

Over $300 worth of savings!

heading: Your neighbourhood electrician

logo

www.wirebrightcrew.com.au
1300 584 672
my pic

Our promise to you...

1.We will arrive on time or we will pay you $100
2.Before any job begins you will know the exact cost
3.We will provide you with a fixed price guarantee assuring no extra costs
4.We will leave your place as clean as when we arrived
5.If there is a problem and it's our fault we will fix it for free
6.We will return your telephone calls promptly
7.We will provide a 12 Month warranty on all parts
8.We will provide friendly, helpful service and advice
..
Nice to have
• on the back of flyer: testimonials..

Here is what some of my customers have had to say...
Very satisfied...
“I am a very satisfied customer!!
Gordon promptly returned by initial email, was very professional in all of his communications
(even ringing me advising me he was going to be running a little late)
Gordon did a fantastic job installing 3 ceiling fans and was very tidy in the process. I have no
hesitation in hiring Gordon in the future, and recommending him to family and friends”.
Rosalind Pemberwick - North Strathfield
Removed all the stress...
What a breath of fresh air...

“Thanks Gordon!
You managed to sort out our electrical problem- this was a problem that another electrician
couldn't resolve after two attempts and a problem which many other electricians shide away
from (messages were left but no one no returned my call).
After eight weeks of stress I contacted Gordon, what a breath of fresh air! Not only did he
give helpful advice over the phone but he was out promptly (and on time) to assess the
problem and provide a written quote. Gordon even contacted us the day before to confirm
the job and was then here on time to start work.
The job was completed in a professional and friendly manner and we haven't had a problem
since.
To top it off Gordon also replaced numerous power points which we had purchased but not
yet installed- all without additional charge. He was clean and tidy- what more could you ask
for. I highly recommend Gordon services whose details I have already given to family and
friends. Thanks Gordon”
Trevor, Helen & Molly - Narwee

Extremely professional...
“Gordon was extremely professional. He arrived when he said he would, quoted the job,
came back with a written quote and was very reasonable. He also checked out our smoke
detectors whist he was here. He installed 2 ceiling fans and an outdoor power point. He
cleaned up the mess and was very efficient. I will definitely use him again and recommend
him to friends”
Yvonne Harker - Croydon

```html
<!DOCTYPE html>
<html lang="en">
<head>
<meta charset="utf-8">
<title>Wirebright Crew – DL Flyer</title>
<link rel="stylesheet" href="https://fonts.googleapis.com/css2?family=Archivo:wght@600;700;800&family=Questrial&family=Open+Sans:ital,wght@0,400;0,600;1,400&display=swap">
<style>
  :root {
    --navy: #1d3a6b;
    --orange: #e8611a;
    --blue: #86acdc;
    --blue-deep: #2b5da0;
    --black: #0d0d0d;
    --paper: #eceef1;
    --paper-dark: #cfd3d8;
    --ink: #1a1a1a;
    --stage: #e4e5e7;
  }
  * { margin: 0; padding: 0; box-sizing: border-box; }
  html, body {
    width: 1169px; height: 1200px; overflow: hidden;
    background: var(--stage);
  }
  .sheet {
    position: absolute; top: 168px;
    width: 406px; height: 862px;
    background: linear-gradient(180deg, var(--paper) 0%, #f6f7f8 50%, var(--paper) 100%);
    overflow: hidden;
    box-shadow: 0 6px 16px rgba(0,0,0,.25);
  }
  .sheet--front { left: 156px; }
  .sheet--back { left: 626px; }
  .sheet__art { position: absolute; inset: 0; width: 100%; height: 100%; }

  /* Front */
  .brand-name {
    position: absolute; left: 8px; top: 58px; width: 96px;
    font-family: "Archivo", sans-serif; font-weight: 800; font-size: 17px;
    line-height: 1.05; color: var(--orange); text-transform: uppercase;
  }
  .headline {
    position: absolute; right: 4px; top: 92px; text-align: right;
    font-family: "Archivo", sans-serif; font-weight: 800; line-height: 1;
  }
  .headline span { display: block; }
  .headline__small { font-size: 25px; color: var(--navy); }
  .headline__big { font-size: 30px; color: var(--orange); margin: 3px 0 2px; }
  .photo {
    position: absolute; left: 61px; top: 186px; width: 256px; height: 268px;
    background: linear-gradient(160deg, #d9dde2 0%, #9aa3ad 45%, #34508f 75%, #1f2f5c 100%);
  }
  .call-badge {
    position: absolute; left: 285px; top: 360px; width: 96px; height: 96px;
    border-radius: 50%; background: var(--orange);
    border: 5px solid #b9bcc0; box-shadow: 0 2px 5px rgba(0,0,0,.35);
    display: flex; flex-direction: column; align-items: center; justify-content: center;
    color: #fff; font-family: "Archivo", sans-serif; font-weight: 700;
    transform: rotate(-25deg);
  }
  .call-badge__icon { width: 18px; height: 18px; margin-bottom: 1px; }
  .call-badge__title { font-size: 15px; line-height: 1; }
  .call-badge__phone { font-size: 12px; line-height: 1.2; }
  .offer-badge {
    position: absolute; left: 6px; top: 444px; width: 64px; height: 64px;
    border-radius: 50%; background: var(--orange); border: 3px solid #fff;
    color: #fff; font-family: "Archivo", sans-serif; font-weight: 700;
    font-size: 14px; line-height: 1.05; text-align: center;
    display: flex; align-items: center; justify-content: center;
    transform: rotate(-20deg);
  }
  .site-url {
    position: absolute; left: 82px; top: 464px;
    font-family: "Archivo", sans-serif; font-weight: 700; font-size: 19.5px;
    color: var(--orange);
  }
  .offers {
    position: absolute; left: 18px; top: 500px; width: 370px; height: 98px;
    background: var(--blue); border-radius: 6px;
    padding: 7px 10px 0 20px;
    font-family: "Archivo", sans-serif; font-weight: 700; color: #fff;
  }
  .offers__row { display: flex; font-size: 13.5px; line-height: 18px; white-space: nowrap; }
  .offers__save { width: 38px; }
  .offers__amount { width: 46px; color: var(--orange); font-size: 16px; }
  .offers__total { text-align: center; color: var(--ink); font-size: 16px; margin-top: 3px; }
  .plug-icon {
    position: absolute; width: 42px; height: 42px; border-radius: 50%;
    background: #fff; border: 3px solid #9aa0a8;
    display: flex; align-items: center; justify-content: center;
  }
  .plug-icon svg { width: 28px; height: 28px; }
  .sheet--front .plug-icon { left: 10px; top: 613px; }
  .promise-title {
    position: absolute; left: 98px; top: 621px;
    font-family: "Questrial", sans-serif; font-size: 21px; color: var(--navy);
  }
  .promise-list {
    position: absolute; left: 28px; top: 662px; width: 370px; list-style: none;
    font-family: "Questrial", sans-serif; font-size: 13.3px; line-height: 18.5px; color: var(--ink);
  }
  .promise-list li { padding-left: 14px; text-indent: -14px; }

  /* Back */
  .section-title {
    position: absolute; left: 4px; top: 92px;
    font-family: "Archivo", sans-serif; font-weight: 800; line-height: 1;
  }
  .section-title span { display: block; }
  .section-title__small { font-size: 23px; color: var(--navy); }
  .section-title__big { font-size: 32px; color: var(--orange); margin-top: 3px; }
  .testimonials {
    position: absolute; left: 11px; top: 178px; width: 392px;
    font-family: "Open Sans", sans-serif; font-size: 11.2px; line-height: 13.9px; color: var(--ink);
  }
  .testimonials p { margin: 0; }
  .testimonials em { font-style: italic; }
  .testimonials .gap { height: 13.9px; }
  .author { display: flex; align-items: center; color: var(--blue-deep); font-style: normal; }
  .author::after { content: ""; flex: 1; height: 2px; background: var(--orange); margin-left: 2px; margin-top: 4px; }
  .sheet--back .plug-icon { left: 349px; top: 808px; }
  .back-url {
    position: absolute; right: 70px; top: 842px;
    font-family: "Archivo", sans-serif; font-weight: 700; font-size: 13px; color: var(--orange);
  }
</style>
</head>
<body>

<section class="sheet sheet--front" aria-label="Flyer front">
  <svg class="sheet__art" viewBox="0 0 406 862" preserveAspectRatio="none" aria-hidden="true">
    <defs>
      <linearGradient id="swoosh-front" x1="0" y1="0" x2="1" y2="0">
        <stop offset="0" stop-color="#ffffff"/>
        <stop offset=".6" stop-color="#b7bcc2"/>
        <stop offset="1" stop-color="#6f757c"/>
      </linearGradient>
    </defs>
    <path d="M0 0 H406 V44 C300 30 170 60 70 120 C40 140 15 160 0 180 Z" fill="var(--black)"/>
    <path d="M0 180 C15 160 40 140 70 120 C170 60 300 30 406 44 V58 C300 48 180 74 80 132 C45 152 18 175 0 196 Z" fill="url(#swoosh-front)"/>
    <path d="M0 720 C80 650 200 640 300 660 C350 670 385 690 406 700 V850 H0 Z" fill="var(--blue)"/>
    <path d="M0 735 C90 665 210 655 310 675 C355 684 388 700 406 710 V850 H0 Z" fill="#a9c4e7" opacity=".6"/>
    <rect x="56" y="644" width="350" height="2.5" fill="var(--orange)"/>
    <rect x="0" y="849" width="406" height="13" fill="var(--orange)"/>
  </svg>

  <div class="brand-name">Wirebright Crew</div>

  <h1 class="headline">
    <span class="headline__small">YOUR</span>
    <span class="headline__big">NEIGHBOURHOOD</span>
    <span class="headline__small">ELECTRICAN</span>
  </h1>

  <div class="photo" role="img" aria-label="Photo of the electrician in a blue polo shirt, arms crossed, standing in front of a white work vehicle"></div>

  <div class="call-badge">
    <svg class="call-badge__icon" viewBox="0 0 24 24" aria-hidden="true"><path fill="#fff" d="M6.6 10.8a15 15 0 0 0 6.6 6.6l2.2-2.2a1 1 0 0 1 1-.25 11.4 11.4 0 0 0 3.6.57 1 1 0 0 1 1 1V20a1 1 0 0 1-1 1A17 17 0 0 1 3 4a1 1 0 0 1 1-1h3.5a1 1 0 0 1 1 1c0 1.25.2 2.45.57 3.57a1 1 0 0 1-.25 1z"/></svg>
    <span class="call-badge__title">CALL NOW</span>
    <span class="call-badge__phone">1300 584 672</span>
  </div>

  <div class="offer-badge">Offer<br>boxes</div>
  <div class="site-url">www.wirebrightcrew.com.au</div>

  <div class="offers">
    <div class="offers__row"><span class="offers__save">Save</span><span class="offers__amount">$97</span><span>complimentry electrical safety inspection</span></div>
    <div class="offers__row"><span class="offers__save">Save</span><span class="offers__amount">$50</span><span>off your job,free power point replacment</span></div>
    <div class="offers__row"><span class="offers__save">Save</span><span class="offers__amount">$150</span><span>OFF switchboard upgrades</span></div>
    <div class="offers__total">Over $300 worth of savings!</div>
  </div>

  <div class="plug-icon">
    <svg viewBox="0 0 32 32" aria-hidden="true"><path fill="var(--navy)" d="M4 15h6v-3h6a5 5 0 0 1 5 4 5 5 0 0 1-5 4h-6v-3H4z M21 13h7v2h-7z M21 17h7v2h-7z"/></svg>
  </div>
  <h2 class="promise-title">OUR PROMISE TO YOU...</h2>

  <ol class="promise-list">
    <li>1.We will arrive on time or we will pay you $100</li>
    <li>2.Before any job begins you will know the exact cost</li>
    <li>3.We will provide you with a fixed price guarantee assuring no extra costs</li>
    <li>4.We will leave your place as clean as when we arrived</li>
    <li>5.If there is a problem and it's our fault we will fix it for free</li>
    <li>6.We will return your telephone calls promptly</li>
    <li>7.We will provide a 12 Month warranty on all parts</li>
    <li>8.We will provide friendly, helpful service and advice</li>
  </ol>
</section>

<section class="sheet sheet--back" aria-label="Flyer back">
  <svg class="sheet__art" viewBox="0 0 406 862" preserveAspectRatio="none" aria-hidden="true">
    <defs>
      <linearGradient id="swoosh-back" x1="0" y1="0" x2="1" y2="0">
        <stop offset="0" stop-color="#6f757c"/>
        <stop offset=".4" stop-color="#b7bcc2"/>
        <stop offset="1" stop-color="#ffffff"/>
      </linearGradient>
    </defs>
    <path d="M0 0 H406 V178 C380 150 350 125 300 100 C220 62 110 44 0 44 Z" fill="var(--black)"/>
    <path d="M0 44 C110 44 220 62 300 100 C350 125 380 150 406 178 V196 C375 165 345 142 290 115 C210 78 105 60 0 58 Z" fill="url(#swoosh-back)"/>
    <path d="M0 770 C100 740 220 745 406 790 V862 H0 Z" fill="var(--blue)"/>
    <rect x="0" y="827" width="350" height="2.5" fill="var(--orange)"/>
  </svg>

  <h2 class="section-title">
    <span class="section-title__small">QUALITY OF</span>
    <span class="section-title__big">OUR SERVICE</span>
  </h2>

  <div class="testimonials">
    <p>Here is what some of my customers have had to say...</p>
    <p><em>Very satisfied...</em></p>
    <p><em>“I am a very satisfied customer!!<br>Gordon promptly returned by initial email, was very professional in all of his communications (even ringing me advising me he was going to be running a little late). Gordon did a fantastic job installing 3 ceiling fans and was very tidy in the process. I have no hesitation in hiring Gordon in the future, and recommending him to family and friends”.</em></p>
    <p class="author">Rosalind Pemberwick - North Strathfield</p>
    <div class="gap"></div>
    <p><em>Removed all the stress...<br>What a breath of fresh air...</em></p>
    <div class="gap"></div>
    <p><em>“Thanks Gordon!<br>You managed to sort out our electrical problem- this was a problem that another electrician couldn't resolve after two attempts and a problem which many other electricians shide away from (messages were left but no one no returned my call).<br>After eight weeks of stress I contacted Gordon, what a breath of fresh air! Not only did he give helpful advice over the phone but he was out promptly (and on time) to assess the problem and provide a written quote. Gordon even contacted us the day before to confirm the job and was then here on time to start work. The job was completed in a professional and friendly manner and we haven't had a problem since.<br>To top it off Gordon also replaced numerous power points which we had purchased but not yet installed- all without additional charge. He was clean and tidy- what more could you ask for. I highly recommend Gordon services whose details I have already given to family and friends. Thanks Gordon”</em></p>
    <p class="author">Trevor, Helen &amp; Molly - Narwee</p>
    <div class="gap"></div>
    <p><em>Extremely professional...<br>“Gordon was extremely professional. He arrived when he said he would, quoted the job, came back with a written quote and was very reasonable. He also checked out our smoke detectors whist he was here. He installed 2 ceiling fans and an outdoor power point. He cleaned up the mess and was very efficient. I will definitely use him again and recommend him to friends”</em></p>
    <p class="author">Yvonne Harker - Croydon</p>
  </div>

  <div class="plug-icon">
    <svg viewBox="0 0 32 32" aria-hidden="true"><path fill="var(--navy)" d="M4 15h6v-3h6a5 5 0 0 1 5 4 5 5 0 0 1-5 4h-6v-3H4z M21 13h7v2h-7z M21 17h7v2h-7z"/></svg>
  </div>
  <div class="back-url">www.wirebrightcrew.com.au</div>
</section>

</body>
</html>
```